Schlichtes Design für Malerbetrieb
Zielgruppe
Wir sind ein mittelgroßer Malerbetrieb in München mit umfangreichem Leistungsspektrum.
Unsere Hauptleistungen sind: Fassadenrenovierung, Altbausanierung, Betoninstandsetzung, Balkonabdichtung (kein Neubau!).
Unsere Zielgruppen sind: Hausverwaltungen, Firmen und Privatpersonen.
Unsere Kunden schätzen: Konstruktive Organisation und Planung im Vorfeld, Zuverlässigkeit, saubere Arbeitsweise, dauerhafte Balkonabdichtungen.
Aufgabenstellung
Wir möchten eine langlebige, stilvolle, minimalistische Homepage.
Wir möchten von der bestehenden Homepage nur die Schriftart für unseren Firmennamen (Century Gothic) und wenn möglich (nicht zwingend), irgendwo das florale Muster einbauen. Corporate-Design haben wir nicht.
Farbtöne: Firmennamen Orange (hellorange bis erdiges Orange möglich, da sind wir nicht fixiert) , einen dunklen Hintergrundfarbton (Petrol-Blaugrau ?) mit gelbem (neon bis senfgelb) Akzent (Linien), Blumenmuster weiß, grau.
Dies sind nur unsere Ideen. Wir sind aber auch absolut offen für eure Profi-Ideen.
Wir möchten uns von den unzähligen langweiligen 'Pinselseiten mit veralteten Bilder' unserer Kollegen interessant und mit Stil abheben.
Eher nach dem Motto 'weniger ist mehr'.
Einen positiven, sympathischen Eindruck geben und unsere Leistungen in den Vordergrund bringen.
Da wir viele Stammkunden haben, betreiben wir kein Social-Media und möchten dies vorerst auch nicht tun.
Die Seite wird in den nächsten Jahren nicht verändert, höchstens die Bilder aktualisiert.
Die Texte haben wir alle selbst entworfen und möchten wir so übernehmen.
Die Galerien sollen unkompliziert anzuschauen sein.
Uns gefällt die Struktur und Schlichtheit von https://vormtakel.nl/ oder Tessuri.de gut und wir mögen Vintage-Grafiken gerne.
Einerseits darf die Seite geradlinig, andererseits aber auch rund und floral wirken.

```html
<!DOCTYPE html>
<html lang="de">
<head>
<meta charset="utf-8">
<title>halvert Malerarbeiten</title>
<link href="https://fonts.googleapis.com/css2?family=Encode+Sans+Semi+Condensed:wght@400&display=swap" rel="stylesheet">
<style>
  :root {
    --bar: #59585a;
    --pattern-bg: #636264;
    --teal: #017a94;
    --mustard: #d9c95a;
    --stone: #9d9ea0;
    --white: #ffffff;
  }
  html, body {
    margin: 0;
    padding: 0;
    width: 1200px;
    height: 900px;
    overflow: hidden;
    background: var(--bar);
  }
  .page {
    position: relative;
    width: 1200px;
    height: 900px;
    overflow: hidden;
    font-family: 'Encode Sans Semi Condensed', sans-serif;
    font-weight: 400;
  }
  .site-header {
    position: absolute;
    top: 0; left: 0;
    width: 1200px;
    height: 127px;
    background: var(--bar);
  }
  .header-name {
    position: absolute;
    right: 52px;
    top: 14px;
    margin: 0;
    font-size: 46px;
    line-height: 1.1;
    color: var(--mustard);
  }
  .main-nav {
    position: absolute;
    left: 42px;
    right: 54px;
    top: 86px;
    display: flex;
    justify-content: space-between;
    font-size: 23px;
    color: var(--white);
  }
  .main-nav a, .footer-nav a {
    color: inherit;
    text-decoration: none;
  }
  .hero {
    position: absolute;
    top: 127px; left: 0;
    width: 1200px;
    height: 717px;
  }
  .hero svg { display: block; }
  .brand {
    position: absolute;
    left: 118px;
    top: 262px;
    margin: 0;
    font-weight: 400;
    color: var(--mustard);
  }
  .brand-name {
    display: block;
    font-size: 104px;
    line-height: 1;
  }
  .brand-tagline {
    display: block;
    margin-top: 10px;
    font-size: 30px;
    line-height: 1;
  }
  .site-footer {
    position: absolute;
    left: 0; bottom: 0;
    width: 1200px;
    height: 56px;
    background: var(--bar);
  }
  .footer-nav {
    position: absolute;
    right: 20px;
    top: 12px;
    display: flex;
    gap: 21px;
    font-size: 25px;
    color: var(--white);
  }
</style>
</head>
<body>
<div class="page">
  <header class="site-header">
    <p class="header-name">halvert</p>
    <nav class="main-nav">
      <a href="#">malerarbeiten</a>
      <a href="#">betoninstandsetzung</a>
      <a href="#">balkonabdichtung</a>
      <a href="#">farbgestaltung</a>
      <a href="#">wärmedämmung</a>
      <a href="#">ausbildung</a>
      <a href="#">portrait</a>
    </nav>
  </header>

  <section class="hero">
    <svg width="1200" height="717" viewBox="0 127 1200 717">
      <rect x="0" y="127" width="1200" height="717" fill="var(--pattern-bg)" role="img" aria-label="Florales Damastmuster in Grautönen als Hintergrund"/>
      <polygon points="598,545 1200,844 404,844 264,709" fill="var(--stone)"/>
      <polygon points="1200,248 1200,844 598,545" fill="var(--mustard)"/>
      <polygon points="0,127 252,127 850,412 0,808" fill="var(--teal)"/>
    </svg>
    <h1 class="brand">
      <span class="brand-name">halvert</span>
      <span class="brand-tagline">Malerarbeiten</span>
    </h1>
  </section>

  <footer class="site-footer">
    <nav class="footer-nav">
      <a href="#">Kontakt</a>
      <a href="#">Impressum</a>
      <a href="#">Datenschutz</a>
    </nav>
  </footer>
</div>
</body>
</html>
```